Business card design

I need a business card design for a teledentistry software company. I will be using tamber ink or a similar service for the printing. Front and back side needed. Logo attached.

```html
<!DOCTYPE html>
<html lang="en">
<head>
<meta charset="utf-8">
<title>Nuvadent Care – Business Card</title>
<link rel="stylesheet" href="https://fonts.googleapis.com/css2?family=Montserrat:wght@400;500;600;700&display=swap">
<style>
  :root {
    --teal: #2bb3a6;
    --teal-deep: #1f9d92;
    --teal-light: #3cc4b6;
    --ink: #3d3d40;
    --ink-soft: #555559;
    --paper: #ffffff;
    --paper-shade: #eeeeee;
    --backdrop: #e4e5e7;
  }
  * { box-sizing: border-box; margin: 0; padding: 0; }
  html, body {
    width: 1200px;
    height: 900px;
    overflow: hidden;
    background: var(--backdrop);
    font-family: "Montserrat", sans-serif;
  }
  .canvas {
    position: relative;
    width: 1200px;
    height: 900px;
  }
  .card {
    position: absolute;
    width: 560px;
    height: 320px;
    border-radius: 22px;
    box-shadow: 0 10px 30px rgba(0, 0, 0, 0.18);
    overflow: hidden;
  }
  .card-front {
    left: 90px;
    top: 110px;
    background: linear-gradient(135deg, var(--teal-deep), var(--teal-light));
    display: flex;
    align-items: center;
    justify-content: center;
    gap: 18px;
  }
  .card-back {
    left: 550px;
    top: 470px;
    background: linear-gradient(180deg, var(--paper), var(--paper-shade));
    display: flex;
    flex-direction: column;
    align-items: center;
    padding-top: 40px;
  }
  .brand-mark {
    width: 22px;
    height: 22px;
    border-radius: 50%;
    background: var(--paper);
    flex: none;
  }
  .brand-name-front {
    color: var(--paper);
    font-weight: 700;
    font-size: 58px;
    letter-spacing: 0.5px;
  }
  .brand-row {
    display: flex;
    align-items: center;
    gap: 10px;
  }
  .brand-row .brand-mark {
    width: 14px;
    height: 14px;
    background: var(--teal);
  }
  .brand-name-back {
    color: var(--ink);
    font-weight: 700;
    font-size: 30px;
  }
  .person-name {
    margin-top: 34px;
    color: var(--teal);
    font-weight: 600;
    font-size: 21px;
  }
  .person-title {
    margin-top: 2px;
    color: var(--ink-soft);
    font-weight: 400;
    font-size: 12px;
  }
  .service-icons {
    display: flex;
    gap: 10px;
    margin-top: 12px;
  }
  .contact {
    margin-top: 12px;
    text-align: center;
    color: var(--ink);
    font-weight: 400;
    font-size: 13px;
    line-height: 1.5;
  }
</style>
</head>
<body>
  <main class="canvas">
    <section class="card card-front" aria-label="Card front">
      <span class="brand-mark"></span>
      <span class="brand-name-front">Nuvadent Care</span>
    </section>

    <section class="card card-back" aria-label="Card back">
      <div class="brand-row">
        <span class="brand-mark"></span>
        <span class="brand-name-back">Nuvadent Care</span>
      </div>
      <p class="person-name">Warren Hale</p>
      <p class="person-title">Executive Director</p>
      <div class="service-icons">
        <svg width="18" height="18" viewBox="0 0 18 18" aria-hidden="true"><circle cx="9" cy="9" r="8" fill="var(--teal)"/></svg>
        <svg width="18" height="18" viewBox="0 0 18 18" aria-hidden="true"><circle cx="9" cy="9" r="8" fill="var(--teal)"/></svg>
        <svg width="18" height="18" viewBox="0 0 18 18" aria-hidden="true"><circle cx="9" cy="9" r="8" fill="var(--teal)"/></svg>
      </div>
      <address class="contact" style="font-style: normal;">
        <div>555-014-2297</div>
        <div>info@brightoakstudio.com</div>
        <div>www.brightoakstudio.com</div>
      </address>
    </section>
  </main>
</body>
</html>
```